Weather card for guests at Fenwick’s Beach House

I am looking to have a card designed for my guests who stay over. The card should show the weather for the next day (emoji's), quote of the day, Activities of the day. It's for a beach house so it should be coastal/Beachy themed. The weather should have a high and a low. (I will fill in each card). It should be front and back. It should be a fun project. Think modern farmhouse. The top of each card should say something like Another great Day at 7 Harbor
Updates

If you google "turn down Service letter" or "hotel weather card". It will provide examples

Target Market(s)

Our guests who visit our beach house

Font styles to use
Sans Serif

Colors
0054AA
0677BA
7BADD7
CADEEF
E8F1F8

Requirements
Must have
• weather options, quote of the day, activity for the day
Nice to have
• Sand, seashells, seagulls
Should not have
• Should not be too busy and not childish

```html
<!DOCTYPE html>
<html lang="en">
<head>
<meta charset="utf-8">
<title>Fenwick’s Beach House – Guest Weather Card</title>
<link rel="stylesheet" href="https://fonts.googleapis.com/css2?family=Quicksand:wght@500;600;700&display=swap">
<style>
  :root {
    --navy: #0054AA;
    --ocean: #0677BA;
    --sky: #7BADD7;
    --mist: #CADEEF;
    --foam: #E8F1F8;
    --backdrop: #ececec;
    --card-top: #b8c3cc;
    --card-mid: #d6dce3;
    --sand: #d2b38c;
  }
  * { box-sizing: border-box; margin: 0; padding: 0; }
  html, body { width: 1200px; height: 993px; overflow: hidden; }
  body {
    background: var(--backdrop);
    position: relative;
    font-family: "Quicksand", "Helvetica Neue", Arial, sans-serif;
    color: var(--navy);
  }
  .card {
    position: absolute;
    width: 518px;
    height: 827px;
    overflow: hidden;
    background: linear-gradient(180deg, var(--card-top) 0%, var(--card-mid) 30%, var(--foam) 55%);
  }
  .card--front { left: 51px; top: 62px; }
  .card--back { left: 631px; top: 103px; }

  .beach-photo {
    position: absolute;
    left: 0; right: 0; bottom: 0;
    background: linear-gradient(180deg, var(--foam) 0%, var(--mist) 35%, #a9c8e4 60%, var(--sand) 85%, var(--sand) 100%);
  }
  .card--front .beach-photo { top: 452px; }
  .card--back .beach-photo { top: 470px; }

  .greeting {
    position: absolute;
    top: 36px; left: 0; right: 0;
    text-align: center;
  }
  .greeting__lead {
    font-size: 30px;
    font-weight: 700;
    line-height: 1;
  }
  .greeting__place {
    font-size: 84px;
    font-weight: 500;
    line-height: 1;
    margin-top: -2px;
    letter-spacing: 1px;
  }

  .section-title {
    position: absolute;
    left: 0; right: 0;
    text-align: center;
    font-size: 20px;
    font-weight: 700;
    line-height: 1;
  }
  .section-title--weather { top: 203px; }
  .section-title--temps { top: 360px; }

  .weather-options {
    position: absolute;
    top: 248px; left: 29px;
    display: flex;
    gap: 19px;
  }
  .weather-tag {
    position: relative;
    width: 77px; height: 77px;
    border-radius: 7px;
    background: var(--sky);
  }
  .weather-tag::before {
    content: "";
    position: absolute;
    top: -11px; left: 50%;
    width: 19px; height: 19px;
    margin-left: -9.5px;
    border-radius: 50%;
    background: #fff;
    border: 2px solid var(--sky);
  }
  .weather-tag svg {
    position: absolute;
    inset: 0;
    width: 77px; height: 77px;
    fill: none;
    stroke: #fff;
    stroke-width: 1.6;
    stroke-linecap: round;
    stroke-linejoin: round;
  }

  .temp-fields {
    position: absolute;
    top: 392px; left: 29px;
    display: flex;
    gap: 21px;
  }
  .temp-field {
    width: 219px; height: 37px;
    border: 2px solid var(--sky);
    border-radius: 7px;
    background: #fff;
    color: var(--sky);
    font-size: 15px;
    font-weight: 700;
    line-height: 33px;
    padding-left: 11px;
  }

  .write-in {
    position: absolute;
    left: 30px;
    width: 456px;
    border: 2px solid var(--sky);
    border-radius: 8px;
    background: rgba(232, 241, 248, 0.35);
  }
  .write-in--quote { top: 43px; height: 189px; }
  .write-in--activities { top: 250px; height: 181px; }
  .write-in__title {
    text-align: center;
    font-size: 20px;
    font-weight: 700;
    line-height: 1;
    margin-top: 9px;
  }
</style>
</head>
<body>

<section class="card card--front" aria-label="Front of guest card">
  <div class="beach-photo" role="img" aria-label="Photo of a seashell resting on sand by the sea"></div>

  <header class="greeting">
    <p class="greeting__lead">Another great day at</p>
    <h1 class="greeting__place">7 Harbor</h1>
  </header>

  <h2 class="section-title section-title--weather">Tomorrow’s Weather</h2>
  <div class="weather-options">
    <div class="weather-tag" aria-label="Sunny">
      <svg viewBox="0 0 77 77">
        <circle cx="38.5" cy="41" r="11"/>
        <path d="M38.5 22v6M38.5 54v6M19.5 41h6M51.5 41h6M25 27.5l4 4M48 50.5l4 4M52 27.5l-4 4M29 50.5l-4 4"/>
      </svg>
    </div>
    <div class="weather-tag" aria-label="Partly cloudy">
      <svg viewBox="0 0 77 77">
        <circle cx="28" cy="37" r="6"/>
        <path d="M28 26v3M17 37h3M20 29l2 2M36 29l-2 2M20 45l2-2"/>
        <path d="M27 58h33a7 7 0 0 0 0-14 10 10 0 0 0-19-3 8 8 0 0 0-14 4 6.5 6.5 0 0 0 0 13z"/>
      </svg>
    </div>
    <div class="weather-tag" aria-label="Cloudy">
      <svg viewBox="0 0 77 77">
        <path d="M22 53h36a7.5 7.5 0 0 0 0-15 11 11 0 0 0-21-3 8.5 8.5 0 0 0-15 5 7 7 0 0 0 0 13z"/>
      </svg>
    </div>
    <div class="weather-tag" aria-label="Rain">
      <svg viewBox="0 0 77 77">
        <path d="M22 50h36a7.5 7.5 0 0 0 0-15 11 11 0 0 0-21-3 8.5 8.5 0 0 0-15 5 7 7 0 0 0 0 13z"/>
        <path d="M27 56c-2 3-2 5 0 5s2-2 0-5zM38.5 56c-2 3-2 5 0 5s2-2 0-5zM50 56c-2 3-2 5 0 5s2-2 0-5z"/>
      </svg>
    </div>
    <div class="weather-tag" aria-label="Snow">
      <svg viewBox="0 0 77 77">
        <path d="M38.5 18v46M18.5 29.5l40 23M18.5 52.5l40-23"/>
        <path d="M34 20l4.5 4 4.5-4M34 62l4.5-4 4.5 4M18 34.5l6-1.5-1.5-6M59 42.5l-6 1.5 1.5 6M22.5 50.5l1.5-6-6-1.5M54.5 26.5l-1.5 6 6 1.5"/>
      </svg>
    </div>
  </div>

  <h2 class="section-title section-title--temps">Temperatures</h2>
  <div class="temp-fields">
    <div class="temp-field">High</div>
    <div class="temp-field">Low</div>
  </div>
</section>

<section class="card card--back" aria-label="Back of guest card">
  <div class="beach-photo" role="img" aria-label="Photo of a seashell resting on sand by the sea"></div>
  <div class="write-in write-in--quote"><h2 class="write-in__title">Quote of the day</h2></div>
  <div class="write-in write-in--activities"><h2 class="write-in__title">Activities for the day</h2></div>
</section>

</body>
</html>
```